Website Re-Design

We would like to explore the possibility of a re-design of our website. We want all the content that it currently has to remain on the pages, and we don't want our logo/corporate identity or colours changed, so it is literally just a website re-design.

Our website is www.drelvix.co.uk

Websites that we like are

http://www.tarnwillow.co.uk/
http://quomplet.com/

```html
<!DOCTYPE html>
<html lang="en">
<head>
<meta charset="utf-8">
<title>Drelvix – Inbound Marketing &amp; SEO Performance Agency</title>
<link rel="stylesheet" href="https://fonts.googleapis.com/css2?family=Source+Sans+3:wght@300;400;600;700&display=swap">
<style>
:root{
  --pink:#e0137e;
  --teal:#17a39b;
  --green:#78b43a;
  --hero-green:#2f5a2c;
  --hero-dark:#1f3d1e;
  --ink:#333333;
  --muted:#8a8a8a;
  --rule:#e2e2e2;
  --band:#f1f1f1;
  --band-light:#f8f8f8;
  --footer:#2d2d2d;
  --footer-text:#9a9a9a;
  --white:#ffffff;
}
*{margin:0;padding:0;box-sizing:border-box}
html,body{width:1200px;height:2483px;overflow:hidden}
body{position:relative;background:var(--white);font-family:"Source Sans 3",sans-serif;color:var(--ink)}
.abs{position:absolute}
a{color:inherit;text-decoration:none}

/* header */
.site-header{left:0;top:0;width:1200px;height:119px;background:var(--white)}
.brand{left:66px;top:34px;font-size:46px;font-weight:700;color:var(--pink);letter-spacing:1px;line-height:1}
.main-nav{left:460px;top:56px;display:flex;font-size:17px;color:#555;text-transform:uppercase}
.main-nav a{padding:0 16px;border-left:1px solid #d6d6d6;line-height:24px}
.main-nav a:first-child{border-left:none}
.talk-btn{left:1031px;top:49px;width:108px;height:36px;background:var(--pink);color:var(--white);font-size:15px;line-height:36px;text-align:center;border-radius:3px;text-transform:uppercase}

/* hero */
.hero{left:0;top:119px;width:1200px;height:470px;background:radial-gradient(ellipse at 30% 50%,#4b7f3a 0%,var(--hero-green) 55%,var(--hero-dark) 100%)}
.hero-band{left:330px;top:157px;width:600px;height:141px;background:linear-gradient(90deg,rgba(20,20,20,0) 0%,rgba(20,20,20,.8) 12%,rgba(20,20,20,.8) 88%,rgba(20,20,20,0) 100%)}
.hero-title{left:0;top:178px;width:1200px;text-align:center;font-size:60px;font-weight:300;color:var(--white);line-height:1}
.hero-title span{color:#8cc63f}
.hero-sub{left:0;top:250px;width:1200px;text-align:center;font-size:17px;color:#e8e8e8;letter-spacing:.5px}
.hero-arrow{top:190px;width:52px;height:52px;border-radius:50%;background:#111}
.hero-arrow.prev{left:35px}
.hero-arrow.next{left:1120px}
.hero-arrow svg{display:block}

/* intro */
.intro-title{left:0;top:650px;width:1200px;text-align:center;font-size:37px;font-weight:300;color:#444}
.intro-title span{color:var(--pink)}
.intro-text{left:0;top:708px;width:1200px;text-align:center;font-size:15.5px;color:#777;line-height:23px}

/* feature columns */
.features{left:0;top:823px;width:1200px;height:443px;background:var(--band);border-top:1px solid #e6e6e6;border-bottom:1px solid #e6e6e6}
.feature{top:870px;width:335px}
.feature h2{font-size:28px;font-weight:300;color:#444;line-height:1}
.feature-image{margin-top:20px;width:331px;height:136px;border:4px solid var(--white);box-shadow:0 1px 3px rgba(0,0,0,.15)}
.feature h3{margin-top:16px;font-size:16px;font-weight:400;color:#555}
.feature p{margin-top:6px;font-size:13.5px;line-height:21px;color:var(--muted)}
.btn{display:inline-block;height:31px;line-height:31px;padding:0 18px;font-size:12px;font-weight:600;color:var(--white);text-transform:uppercase;border-radius:2px}
.feature .btn{margin-top:14px}
.btn.pink{background:var(--pink)}
.btn.green{background:var(--green)}
.btn.teal{background:var(--teal)}

/* recent works */
.works-title{left:83px;top:1355px;font-size:40px;font-weight:300;color:var(--teal)}
.works-lead{left:74px;top:1408px;font-size:19px;color:#444}
.works-text{left:74px;top:1438px;width:460px;font-size:14.5px;line-height:29.5px;color:#777}
.dots{left:84px;top:1572px;display:flex;gap:6px}
.dots i{width:16px;height:16px;border-radius:50%;background:#d8d8d8}
.dots i.on{background:var(--teal)}
.tablet{left:640px;top:1316px;width:466px;height:347px;border-radius:18px;background:linear-gradient(#fbfbfb,#e9e9e9);border:1px solid #d2d2d2;box-shadow:0 10px 18px rgba(0,0,0,.12)}
.tablet-screen{left:683px;top:1351px;width:380px;height:272px;background:linear-gradient(135deg,#e9f1fa 0%,#b9d3ee 55%,#5d88c2 100%)}
.tablet-cam{left:659px;top:1483px;width:7px;height:7px;border-radius:50%;background:#bfbfbf}

/* contact + clients */
.cta-band{left:0;top:1721px;width:1200px;height:343px;background:var(--band-light)}
.cta-title{left:69px;top:1782px;font-size:32px;font-weight:300;color:var(--pink)}
.cta-text{left:69px;top:1829px;width:430px;font-size:14px;line-height:23px;color:#666}
.cta-text .tail{display:block;margin-top:4px;color:#444}
.cta-btn{left:68px;top:1916px;height:37px;line-height:37px;padding:0 20px;font-size:14px}
.clients-title{left:612px;top:1782px;font-size:32px;font-weight:300;color:var(--teal)}
.clients-text{left:614px;top:1829px;width:500px;font-size:14px;line-height:23px;color:#666}
.clients-text .tail{display:block;margin-top:4px;color:#444}
.clients{left:612px;top:1945px;width:540px;display:flex;justify-content:space-between;align-items:center}
.client{display:flex;align-items:center;gap:6px;font-size:17px;font-weight:600;color:#555}
.client i{width:16px;height:16px;border-radius:50%;background:var(--teal)}

/* footer */
.site-footer{left:0;top:2064px;width:1200px;height:419px;background:var(--footer)}
.f-col{top:2108px}
.f-col h4{font-size:17px;font-weight:400;color:var(--white);text-transform:uppercase;padding-bottom:8px;border-bottom:1px solid #444}
.f-col ul{list-style:none;margin-top:10px}
.f-col li{font-size:14px;line-height:31px;color:#ccc;text-transform:uppercase}
.f-col p{margin-top:12px;font-size:13px;line-height:25px;color:var(--footer-text)}
.f-col .contact{color:#ccc;font-size:14px}
.socials{margin-top:14px;display:flex;gap:5px}
.socials i{width:29px;height:29px;border-radius:50%;background:#8cc63f}
.f-rule{left:70px;top:2408px;width:1082px;height:1px;background:#444}
.copyright{left:70px;top:2434px;font-size:13px;color:#777}
</style>
</head>
<body>

<header class="site-header abs">
  <div class="brand abs">DRELVIX</div>
  <nav class="main-nav abs">
    <a href="#">Home</a><a href="#">About</a><a href="#">Portfolio</a><a href="#">What we do</a><a href="#">Contact us</a>
  </nav>
  <a class="talk-btn abs" href="#">Talk to us</a>
</header>

<section class="hero abs" role="img" aria-label="Illustration of a hand holding a megaphone against a green pattern of eco and social icons"></section>
<div class="hero-band abs"></div>
<h1 class="hero-title abs">Search.<span>Social</span>.Media</h1>
<div class="hero-sub abs">PHASELLUS FELIS DOLOR SCELERISQUE A TEMPUS EGET LOBORTIS</div>
<a class="hero-arrow prev abs" href="#" aria-label="Previous slide"><svg width="52" height="52" viewBox="0 0 52 52"><path d="M29 18l-8 8 8 8" fill="none" stroke="#fff" stroke-width="2"/></svg></a>
<a class="hero-arrow next abs" href="#" aria-label="Next slide"><svg width="52" height="52" viewBox="0 0 52 52"><path d="M23 18l8 8-8 8" fill="none" stroke="#fff" stroke-width="2"/></svg></a>

<h2 class="intro-title abs"><span>Drelvix – your inbound marketing</span> &amp; SEO performance agency</h2>
<p class="intro-text abs">Do you want to earn your customers attention? Gain more visibility in the SERPs and build &amp; engage with your audience?<br>Drelvix specialises in SEO, Social media, CRO and Design &amp; Creative services. Offering a bespoke and personal service from a team of digital natives.</p>

<section class="features abs"></section>
<article class="feature abs" style="left:74px">
  <h2>What can we do for you?</h2>
  <div class="feature-image" role="img" aria-label="Hand sketching a marketing strategy diagram on a whiteboard" style="background:linear-gradient(135deg,#eef3f7,#c9d6e0)"></div>
  <h3>Libero id ullamcorper nonummy</h3>
  <p>Nibh ligula pulvinar metus, eget consectetuer augue nisi quis lacus. Ut ac mi quis lacus mollis aliquam. Curabitur iaculis tempus eros.</p>
  <a class="btn pink" href="#">Read more</a>
</article>
<article class="feature abs" style="left:432px">
  <h2>See our portfolio</h2>
  <div class="feature-image" role="img" aria-label="Colourful grid of flat app interface tiles" style="background:linear-gradient(135deg,#f2b233,#e0503c 40%,#3aa6c9 75%,#8cc63f)"></div>
  <h3>Libero id ullamcorper nonummy</h3>
  <p>Nibh ligula pulvinar metus, eget consectetuer augue nisi quis lacus. Ut ac mi quis lacus mollis aliquam. Curabitur iaculis tempus eros.</p>
  <a class="btn green" href="#">Read more</a>
</article>
<article class="feature abs" style="left:788px">
  <h2>Let’s talk</h2>
  <div class="feature-image" role="img" aria-label="Photo of a support agent wearing a headset" style="background:linear-gradient(90deg,#3f86b5,#8fc0df 60%,#d9c2b0)"></div>
  <h3>Libero id ullamcorper nonummy</h3>
  <p>Nibh ligula pulvinar metus, eget consectetuer augue nisi quis lacus. Ut ac mi quis lacus mollis aliquam. Curabitur iaculis tempus eros.</p>
  <a class="btn teal" href="#">Read more</a>
</article>

<h2 class="works-title abs">Recent Works</h2>
<p class="works-lead abs">Check out our recent works and case-studies.</p>
<p class="works-text abs">These are a few examples to show the diversity of work that we can do to earn real attention, generate inbound links, mentions, citations and be used across many of our marketing channels. See more on our portfolio page and learn about what we could do for you.</p>
<div class="dots abs"><i class="on"></i><i></i><i></i><i></i></div>
<div class="tablet abs"></div>
<div class="tablet-cam abs"></div>
<div class="tablet-screen abs" role="img" aria-label="Screenshot of a recent client website shown on the tablet"></div>

<section class="cta-band abs"></section>
<h2 class="cta-title abs">Sound Intresting?</h2>
<p class="cta-text abs">Are you looking for a progressive and innovative inbound marketing agency who can work alongside your existing teams.<span class="tail">If Yes, then let's have a chat.</span></p>
<a class="btn pink cta-btn abs" href="#">Contact us</a>
<h2 class="clients-title abs">Our Clients &amp; Partners</h2>
<p class="clients-text abs">We work with and represent a number of progressive companies in their SEO, social, inbound marketing, content and strategy needs.<span class="tail">Check out our case-studies for examples.</span></p>
<div class="clients abs">
  <span class="client"><i></i>Brindlemart</span>
  <span class="client"><i></i>Coachwell</span>
  <span class="client"><i></i>Wayfarely</span>
  <span class="client"><i></i>Staynest</span>
</div>

<footer class="site-footer abs"></footer>
<div class="f-col abs" style="left:76px;width:190px">
  <h4>Usefull links</h4>
  <ul><li>Home</li><li>About</li><li>Portfolio</li><li>What we do</li><li>Contact us</li></ul>
</div>
<div class="f-col abs" style="left:301px;width:245px">
  <h4>About us</h4>
  <p>Drelvix is an inbound marketing agency offering a raft of services from digital strategy and planning through to SEO, Social media, SMM, CRO, Design &amp; Creative, through to paid for performance campaigns.</p>
</div>
<div class="f-col abs" style="left:596px;width:225px">
  <h4>Where are we?</h4>
  <p>We are in London, UK, based down the best mews in Canal Row, so come check it out and walk the canals with us or we're happy to venture to you!</p>
</div>
<div class="f-col abs" style="left:885px;width:245px">
  <h4>Contact info</h4>
  <p class="contact">7 Harlow Yard, Canal Row,<br>London, UK, W3 8QT<br>Phone: +44 (0) 207 555 0148<br>Email: hello@drelvix.co.uk</p>
  <div class="socials"><i></i><i></i><i></i><i></i></div>
</div>
<div class="f-rule abs"></div>
<div class="copyright abs">© 2013 Company Name.&nbsp; All right reserved.&nbsp; Term of Use</div>

</body>
</html>
```